card design for engineering consultancy

engineering drafting and project management company the provides drafting services for.
Electrical, Hydraulic, Mechanical, and Civil services
The company is called Q7R Services and logo is as attached
Information on card should be.
1. Logo
2.website : Q7RServices.example
3. email : info@Q7RServices.example
4. Phone: (+61) 400512836
5. Motto: Design - Document - Develop - Deliver

this card should be basically used for business identification only

Target Market(s)

electricians plumbers air conditioning installers and civil contractors

Industry/Entity Type

engineering, drafting, electrical, plumbing, airconditioning, civil

Contact Information for Business Card

1. Logo 2.website : Q7RServices.example 3. email : info@Q7RServices.example 4. Phone: (+61) 400512836 5. Motto: Design - Document - Develop - Deliver

Font styles to use
Serif

Requirements
Must have
• logo
Nice to have
• something inovative and different that makes it stand out from being just another business card

```html
<!DOCTYPE html>
<html lang="en">
<head>
<meta charset="utf-8">
<title>Q7R Services – Business Card</title>
<link href="https://fonts.googleapis.com/css2?family=Michroma&family=Open+Sans:wght@600;700&display=swap" rel="stylesheet">
<style>
  :root {
    --brand-red: #d42535;
    --brand-grey: #4d4d4d;
    --paper: #ffffff;
  }
  html, body {
    margin: 0;
    padding: 0;
    overflow: hidden;
    background: var(--paper);
  }
  .canvas {
    position: relative;
    width: 1139px;
    height: 1200px;
    overflow: hidden;
    background: var(--paper);
  }
  .card-shapes {
    position: absolute;
    inset: 0;
  }
  .accent-red { fill: var(--brand-red); }
  .accent-grey { fill: var(--brand-grey); }

  .brand-name {
    position: absolute;
    margin: 0;
    font-family: "Michroma", "Open Sans", sans-serif;
    font-weight: 400;
    color: var(--brand-grey);
    white-space: nowrap;
    letter-spacing: 0.06em;
  }
  .front-name {
    left: 0;
    width: 1139px;
    top: 330px;
    text-align: center;
    font-size: 46px;
    padding-left: 20px;
    box-sizing: border-box;
  }
  .back-identity {
    position: absolute;
    left: 208px;
    top: 800px;
    width: 240px;
    text-align: center;
  }
  .back-name {
    position: static;
    font-size: 22px;
    letter-spacing: 0.05em;
  }
  .motto {
    margin: 10px 0 0;
    font-family: "Open Sans", sans-serif;
    font-weight: 700;
    font-size: 10.5px;
    color: var(--brand-grey);
    white-space: nowrap;
  }
  .divider {
    position: absolute;
    left: 464px;
    top: 762px;
    width: 6px;
    height: 138px;
    border-radius: 3px;
    background: var(--brand-grey);
  }
  .contact-list {
    position: absolute;
    left: 490px;
    top: 778px;
    margin: 0;
    padding: 0;
    list-style: none;
    font-family: "Open Sans", sans-serif;
    font-weight: 700;
    font-size: 21px;
    color: var(--brand-grey);
  }
  .contact-item {
    display: flex;
    align-items: center;
    gap: 12px;
    height: 34px;
  }
  .contact-icon {
    width: 24px;
    height: 24px;
    flex: none;
  }
  .contact-icon .disc { fill: var(--brand-grey); }
  .contact-icon .glyph { fill: var(--paper); }
  .contact-icon .glyph-line { fill: none; stroke: var(--paper); stroke-width: 1.4; }
</style>
</head>
<body>
<main class="canvas">
  <svg class="card-shapes" width="1139" height="1200" viewBox="0 0 1139 1200" aria-hidden="true">
    <!-- front face -->
    <polygon class="accent-red" points="139,101 989,101 989,571 830,571 896,166 139,166"/>
    <polygon class="accent-grey" points="139,485 781,485 768,571 139,571"/>
    <!-- back face -->
    <polygon class="accent-red" points="139,595 989,595 989,1066 830,1066 896,661 139,661"/>
    <polygon class="accent-grey" points="139,979 781,979 768,1066 139,1066"/>
  </svg>

  <section class="card-front">
    <h1 class="brand-name front-name">Q7R SERVICES</h1>
  </section>

  <section class="card-back">
    <div class="back-identity">
      <p class="brand-name back-name">Q7R SERVICES</p>
      <p class="motto">Design - Document - Develop - Deliver</p>
    </div>
    <div class="divider"></div>
    <ul class="contact-list">
      <li class="contact-item">
        <svg class="contact-icon" viewBox="0 0 24 24" aria-hidden="true">
          <circle class="disc" cx="12" cy="12" r="12"/>
          <circle class="glyph-line" cx="12" cy="12" r="6"/>
          <ellipse class="glyph-line" cx="12" cy="12" rx="2.6" ry="6"/>
          <line class="glyph-line" x1="6" y1="12" x2="18" y2="12"/>
        </svg>
        <span>Q7RServices.example</span>
      </li>
      <li class="contact-item">
        <svg class="contact-icon" viewBox="0 0 24 24" aria-hidden="true">
          <circle class="disc" cx="12" cy="12" r="12"/>
          <rect class="glyph" x="6" y="7.5" width="12" height="9" rx="1.2"/>
          <polyline class="glyph-line" style="stroke: var(--brand-grey)" points="6.5,8.5 12,12.5 17.5,8.5"/>
        </svg>
        <span>info@Q7RServices.example</span>
      </li>
      <li class="contact-item">
        <svg class="contact-icon" viewBox="0 0 24 24" aria-hidden="true">
          <circle class="disc" cx="12" cy="12" r="12"/>
          <path class="glyph" d="M8.2 6.2c.5-.4 1.2-.3 1.5.2l1.3 2.1c.3.5.2 1.1-.2 1.4l-.9.7c.6 1.4 1.7 2.6 3.1 3.3l.7-.9c.4-.4 1-.5 1.4-.2l2.1 1.3c.5.3.6 1 .2 1.5l-.9 1.1c-.5.6-1.3.8-2 .6-3.5-1.1-6.2-3.9-7.2-7.4-.2-.7 0-1.5.6-2z"/>
        </svg>
        <span>(+61) 400512836</span>
      </li>
    </ul>
  </section>
</main>
</body>
</html>
```